Marlowick community hall home page

We are building a modern, responsive website & booking system for our community hall. For this PixelForge task, we would like to receive design ideas for the home page.
There are no limits on the colours or fonts that can be used. We are looking for a modern, fresh design with a local/community feel. We don’t have a logo but we also recognise that our name is quite long! … So initials (MCH) instead of the name would be fine.
People book our community hall for a range of activities including: fitness classes, wedding receptions, birthday parties, business meetings, teaching, community events, charity fundraisers and other celebrations.
We have three main goals for the website. The first is that people can check our calendar and make a booking for an available time slot. The second is that they can read about our facilities and the prices for hiring them. The third is that people can find out about upcoming activities & events.
CTA: Book now
A button that links to a booking request form. (The form is not part of this design project)
Primary/Header navigation:
Home | Calendar | Facilities | Prices | Photos | News | Contact
Secondary/Footer navigation:
Chatterleaf | Quillcast
Login | Register | Privacy policy | Terms & conditions
Example texts (lorem ipsum etc. is also fine):
We have everything you need from a venue, whether it’s an elegant room with ample flexible space, a lavish and elegant hall for a wedding reception, a conference room that fits 125 delegates or a easy access venue to the town centre.
The hall is available for hire for wedding receptions, birthday celebrations, anniversaries, children's parties, presentations, lectures, fitness groups, and will comfortably accommodate all your guests.
This venue is well equipped with a modern kitchen, a range of audio and technical services, hearing loop, licensed bar, conference facilities, disabled access and unlimited free WiFi.
You can use this website to find out more about our rooms, equipment and the services we can offer and use the calendar to see where we have rooms available. You can also book rooms using our online booking system.
To the front of the building is a large public open grassed area across which is a row of shops. To the rear of the building is the large car park, including spaces for blue badge holders and a large enclosed cycle rack. This area also has extensive gardens, with seating and planting areas maintained by local volunteers.
The community hall is run and managed by volunteers of the Marlowick Community Organisation. Our objectives are to increase opportunities for people living in and around Marlowick.
We are passionate about being the heart of the community; caring for this community centred property and visitors are at the heart of all we do.
Where to go next
— Check when the hall is free
— Read our booking policy documents
— Make a booking reservation
Amenities
— Free WiFi
— Free car parking
— Fully equipped kitchen
— Hearing loop
Details for our most popular facilities (rooms):
Name: Main hall
Short description: A 127 square metre main hall with entrance lobby, toilets, a well-equipped kitchen and separate storage facilities. Three sets of double doors provide access to a large paved area and the adjacent playing field.
Capacity: 180 people
Price: £10-20 per hour
Links: More info | Book now
Name: Large meeting room
Short description: A delightful, spacious room with an outlook and access to the small walled garden. Ideal for meetings and small gatherings - it has its own access door and the use of a disabled W/C. We offer a reduced rate for this room when booked together with the main hall.
Capacity: 20 people
Price: £6-12 per hour
Attachments:
We have attached some photos of the hall & some (royalty free) stock images for inspiration.

```html
<!DOCTYPE html>
<html lang="en">
<head>
<meta charset="utf-8">
<title>Marlowick Community Hall</title>
<link rel="stylesheet" href="https://fonts.googleapis.com/css2?family=Merriweather:wght@400;700&family=Montserrat:wght@400;500;600;700&display=swap">
<style>
:root{
  --navy:#0e2d66;
  --navy-deep:#0a2456;
  --blue:#1c4f9e;
  --ink:#555b66;
  --ink-dark:#1f2633;
  --grey:#ececec;
  --card:#f2f2f2;
  --white:#ffffff;
}
*{margin:0;padding:0;box-sizing:border-box}
html,body{width:1200px;height:4341px;overflow:hidden}
body{font-family:'Montserrat',sans-serif;color:var(--ink);background:var(--white);position:relative}
.serif{font-family:'Merriweather',serif}
section,header,footer{position:relative;width:1200px}
.abs{position:absolute}
.rule{position:absolute;height:3px;width:64px;background:var(--navy)}
.btn{position:absolute;display:flex;align-items:center;justify-content:center;font-size:14px;font-weight:500;letter-spacing:.3px}

/* header */
.site-header{height:88px;background:var(--white)}
.brand{position:absolute;left:111px;top:33px;display:flex;align-items:center;gap:10px;color:var(--blue);font-family:'Montserrat',sans-serif;font-weight:600;font-size:16px;line-height:20px;white-space:nowrap}
.brand-mark{display:block;width:14px;height:14px;background:currentColor}
.main-nav{position:absolute;top:34px;left:0;font-size:14px;color:var(--ink-dark)}
.main-nav a{position:absolute;white-space:nowrap;color:inherit;text-decoration:none}
.main-nav a.active{color:var(--blue)}

/* hero */
.hero{height:593px;background:linear-gradient(180deg,#4a4845 0%,#5d5a55 40%,#6c6862 70%,#4f4c48 100%)}
.hero-shade{position:absolute;inset:0;background:rgba(20,20,20,.35)}
.hero-kicker{left:111px;top:278px;font-size:23px;font-weight:700;color:var(--white)}
.hero-title{left:111px;top:306px;font-size:50px;color:var(--white);white-space:nowrap}
.hero-lede{left:111px;top:394px;width:540px;font-size:13.5px;line-height:16px;color:var(--white)}
.btn-book{left:111px;top:447px;width:150px;height:38px;background:var(--blue);color:var(--white)}
.btn-learn{left:280px;top:447px;width:146px;height:38px;border:2px solid var(--white);color:var(--white)}

/* intro */
.intro{height:750px}
.intro-photo{left:111px;top:89px;width:418px;height:573px;background:linear-gradient(180deg,#2b3f8c 0%,#a48a4a 35%,#d9d6cf 65%,#3a4a6e 100%);box-shadow:0 14px 30px rgba(0,0,0,.25)}
.intro-title{left:613px;top:146px;font-size:45px;line-height:54px;color:var(--navy);font-weight:700}
.body-copy{font-size:13px;line-height:26.5px;color:var(--ink)}
.intro-copy{left:613px;top:310px;width:462px}
.btn-read{left:613px;top:559px;width:123px;height:40px;border:2px solid var(--blue);color:var(--blue)}

/* rooms */
.rooms{height:556px;background:var(--navy)}
.rooms-photo{left:586px;top:0;width:614px;height:556px;background:linear-gradient(180deg,#2a1f6e 0%,#6d4a8a 25%,#b9aeb2 55%,#4a3a3a 100%)}
.rooms-kicker{left:111px;top:62px;font-size:19px;color:var(--white)}
.rooms-title{left:111px;top:94px;font-size:45px;font-weight:700;color:var(--white)}
.rooms .rule{background:var(--white);left:111px;top:163px}
.rooms-copy{left:111px;top:204px;width:430px;color:var(--white)}
.btn-more{left:111px;top:450px;width:122px;height:38px;border:2px solid var(--white);color:var(--white)}

/* about */
.about{height:529px;text-align:center}
.about-title{left:0;width:1200px;top:88px;font-size:37px;line-height:43px;font-weight:700;color:var(--navy)}
.about .rule{left:568px;top:196px}
.about-copy{left:150px;width:900px;top:236px}

/* next steps */
.next{height:453px;background:var(--grey)}
.next-photo{left:0;top:0;width:586px;height:453px;background:linear-gradient(180deg,#7a8c6a 0%,#a5553a 30%,#6f8a3d 65%,#6a9a3a 100%)}
.feature-icon{position:absolute;width:68px;height:68px}
.feature-title{position:absolute;left:753px;font-size:31px;color:var(--navy)}
.check-list{position:absolute;left:757px;list-style:none;font-size:13.5px;color:var(--ink)}
.check-list li{display:flex;align-items:center;height:26px}
.check-list svg{width:15px;height:15px;margin-right:9px;flex:none}

/* facilities */
.facilities{height:951px}
.fac-kicker{left:0;width:1200px;text-align:center;top:86px;font-size:19px;color:var(--navy)}
.fac-title{left:0;width:1200px;text-align:center;top:112px;font-size:39px;font-weight:700;color:var(--navy)}
.facilities .rule{left:568px;top:175px}
.card{position:absolute;top:244px;width:391px;height:619px;background:var(--card)}
.card-photo{height:250px}
.card-body{padding:22px 31px 0}
.card-name{font-size:18px;font-weight:600;color:var(--navy);margin-bottom:12px}
.card-desc{font-size:13.5px;line-height:26px;height:174px}
.card-meta{font-size:14.5px;line-height:27px}
.card-meta b{color:var(--ink-dark);font-weight:600}
.card-actions{display:flex;gap:20px;margin-top:14px}
.card-actions span{display:flex;align-items:center;justify-content:center;height:29px;font-size:13.5px}
.link-more{width:103px;border:1px solid #b9bcc2;color:#7b808a}
.link-book{width:106px;background:var(--navy);color:var(--white)}

/* footer */
.site-footer{height:353px;background:var(--navy)}
.site-footer .brand{top:72px;color:var(--white)}
.footer-blurb{left:111px;top:143px;width:250px;font-size:13px;line-height:15.5px;letter-spacing:1px;color:var(--white)}
.footer-col{position:absolute;top:64px;color:var(--white)}
.footer-col h4{font-size:15px;font-weight:600;letter-spacing:2px;margin-bottom:18px}
.footer-col ul{list-style:none;font-size:14px;font-weight:600;line-height:26.5px}
.contact-list li{display:flex;align-items:center}
.contact-list svg{width:16px;height:16px;margin-right:14px;flex:none}
.social{display:flex;gap:16px;margin-top:8px}
.social span{display:flex;align-items:center;gap:6px;font-size:12.5px;font-weight:500}
.social i{display:block;width:16px;height:16px;border:1.5px solid var(--white);border-radius:50%}
.legal{height:68px;background:var(--navy-deep);text-align:center;font-size:12.5px;line-height:68px;letter-spacing:1px;color:#3f5b94}
</style>
</head>
<body>

<header class="site-header">
  <div class="brand"><span class="brand-mark"></span>Marlowick Community Hall</div>
  <nav class="main-nav">
    <a class="active" style="left:465px">Home</a>
    <a style="left:551px">Calendar</a>
    <a style="left:666px">Facilities</a>
    <a style="left:771px">Prices</a>
    <a style="left:856px">Photos</a>
    <a style="left:949px">News</a>
    <a style="left:1031px">Contact</a>
  </nav>
</header>

<section class="hero" role="img" aria-label="Hall interior dressed for a wedding reception with white chairs and floral arrangements">
  <div class="hero-shade"></div>
  <div class="abs hero-kicker serif">We Have Everything</div>
  <h1 class="abs hero-title serif" style="font-weight:400">You Need From A Venue</h1>
  <p class="abs hero-lede">Lorem ipsum dolor sit amet, consectetur adipiscing elit, sed do eiusmod tempor incididunt ut labore et dolore magna aliqua.</p>
  <span class="btn btn-book">BOOK NOW</span>
  <span class="btn btn-learn">LEARN MORE</span>
</section>

<section class="intro">
  <div class="abs intro-photo" role="img" aria-label="Main hall laid with round tables, blue chairs, chandelier and stained glass windows"></div>
  <h2 class="abs intro-title serif">Phasellus Sit Amet<br>Massa Tincidunt</h2>
  <div class="rule" style="left:613px;top:270px"></div>
  <div class="abs intro-copy body-copy">
    <p>Whether it’s an elegant room with ample flexible space, a lavish and elegant hall for a wedding reception, a conference room that fits 125 delegates or a easy access venue to the town centre.</p>
    <p style="margin-top:26px">The hall is available for hire for wedding receptions, birthday celebrations, anniversaries, children’s parties, presentations, lectures, fitness groups, and will comfortably accommodate all your guests.</p>
  </div>
  <span class="btn btn-read">Read More</span>
</section>

<section class="rooms">
  <div class="abs rooms-kicker serif">Find Out More</div>
  <h2 class="abs rooms-title serif">About Our Rooms</h2>
  <div class="rule"></div>
  <div class="abs rooms-copy body-copy">
    <p>This venue is well equipped with a modern kitchen, a range of audio and technical services, hearing loop, licensed bar, conference facilities, disabled access and unlimited free WiFi.</p>
    <p style="margin-top:26px">You can use this website to find out more about our rooms, equipment and the services we can offer and use the calendar to see where we have rooms available.<br>You can also book rooms using our online booking system.</p>
  </div>
  <span class="btn btn-more">More Info</span>
  <div class="abs rooms-photo" role="img" aria-label="Guests seated at round tables in the hall under purple lighting"></div>
</section>

<section class="about">
  <h2 class="abs about-title serif">Phasellus Sit Amet<br>Massa Tincidunt</h2>
  <div class="rule"></div>
  <div class="abs about-copy body-copy">
    <p>To the front of the building is a large public open grassed area across which is a row of shops. To the<br>rear of the building is the large car park, including spaces for blue badge holders and a large enclosed cycle rack.<br>This area also has extensive gardens, with seating and planting areas maintained by local volunteers.</p>
    <p style="margin-top:26px">The community hall is run and managed by volunteers of the Marlowick Community Organisation.<br>Our objectives are to increase opportunities for people living in and around Marlowick.<br>We are passionate about being the heart of the community; caring for this community<br>centred property and visitors are at the heart of all we do.</p>
  </div>
</section>

<section class="next">
  <div class="abs next-photo" role="img" aria-label="Red brick hall building behind a lawn and garden trees"></div>
  <svg class="feature-icon" style="left:657px;top:67px" viewBox="0 0 68 68" fill="none" stroke="#0e2d66" stroke-width="2.5">
    <rect x="4" y="10" width="56" height="50" rx="4"/>
    <line x1="4" y1="22" x2="60" y2="22"/>
    <line x1="16" y1="4" x2="16" y2="14"/><line x1="28" y1="4" x2="28" y2="14"/><line x1="40" y1="4" x2="40" y2="14"/><line x1="52" y1="4" x2="52" y2="14"/>
    <rect x="11" y="29" width="7" height="6"/><rect x="23" y="29" width="7" height="6"/><rect x="35" y="29" width="7" height="6"/><rect x="47" y="29" width="7" height="6"/>
    <rect x="11" y="41" width="7" height="6"/><rect x="23" y="41" width="7" height="6"/><rect x="35" y="41" width="7" height="6"/>
    <circle cx="54" cy="54" r="11" fill="#ececec"/><polyline points="54,48 54,54 59,57"/>
  </svg>
  <h3 class="feature-title serif" style="top:65px;font-weight:400">Where To Go Next?</h3>
  <ul class="check-list" style="top:120px">
    <li><svg viewBox="0 0 15 15" fill="none" stroke="#0e2d66" stroke-width="1.6"><rect x="1" y="2" width="11" height="11"/><polyline points="4,7 6.5,10 14,2"/></svg>Check when the hall is free</li>
    <li><svg viewBox="0 0 15 15" fill="none" stroke="#0e2d66" stroke-width="1.6"><rect x="1" y="2" width="11" height="11"/><polyline points="4,7 6.5,10 14,2"/></svg>Read our booking policy documents</li>
    <li><svg viewBox="0 0 15 15" fill="none" stroke="#0e2d66" stroke-width="1.6"><rect x="1" y="2" width="11" height="11"/><polyline points="4,7 6.5,10 14,2"/></svg>Make a booking reservation</li>
  </ul>
  <svg class="feature-icon" style="left:657px;top:236px" viewBox="0 0 68 68" fill="none" stroke="#0e2d66" stroke-width="2.5">
    <rect x="2" y="4" width="64" height="60" rx="4"/>
    <line x1="2" y1="16" x2="66" y2="16"/>
    <circle cx="9" cy="10" r="1.5"/><circle cx="15" cy="10" r="1.5"/><circle cx="21" cy="10" r="1.5"/>
    <rect x="9" y="24" width="18" height="16"/><line x1="9" y1="48" x2="27" y2="48"/><line x1="9" y1="55" x2="22" y2="55"/>
    <path d="M35 30 q8 -6 16 0"/><path d="M39 34 q4 -3 8 0"/><circle cx="43" cy="38" r="1.5"/>
    <rect x="34" y="46" width="14" height="10"/><polyline points="52,50 55,54 61,44"/>
  </svg>
  <h3 class="feature-title serif" style="top:234px;font-weight:400">Amenities</h3>
  <ul class="check-list" style="top:288px">
    <li><svg viewBox="0 0 15 15" fill="none" stroke="#0e2d66" stroke-width="1.6"><rect x="1" y="2" width="11" height="11"/><polyline points="4,7 6.5,10 14,2"/></svg>Free WiFi</li>
    <li><svg viewBox="0 0 15 15" fill="none" stroke="#0e2d66" stroke-width="1.6"><rect x="1" y="2" width="11" height="11"/><polyline points="4,7 6.5,10 14,2"/></svg>Free car parking</li>
    <li><svg viewBox="0 0 15 15" fill="none" stroke="#0e2d66" stroke-width="1.6"><rect x="1" y="2" width="11" height="11"/><polyline points="4,7 6.5,10 14,2"/></svg>Fully equipped kitchen</li>
    <li><svg viewBox="0 0 15 15" fill="none" stroke="#0e2d66" stroke-width="1.6"><rect x="1" y="2" width="11" height="11"/><polyline points="4,7 6.5,10 14,2"/></svg>Hearing loop</li>
  </ul>
</section>

<section class="facilities">
  <div class="abs fac-kicker serif">Details For Our</div>
  <h2 class="abs fac-title serif">Most Popular Facilities</h2>
  <div class="rule"></div>

  <article class="card" style="left:195px">
    <div class="card-photo" role="img" aria-label="Victorian red brick hall facade against a blue sky" style="background:linear-gradient(180deg,#3d6fb8 0%,#a2502f 50%,#5d7a3a 100%)"></div>
    <div class="card-body">
      <h3 class="card-name">Main Hall</h3>
      <p class="card-desc">A 127 square metre main hall with entrance lobby, toilets, a well-equipped kitchen and separate storage facilities. Three sets of double doors provide access to a large paved area and the adjacent playing field.</p>
      <p class="card-meta"><b>Capacity:</b> 180 people<br><b>Price:</b> £10-20 per hour</p>
      <div class="card-actions"><span class="link-more">More Info</span><span class="link-book">Book Now</span></div>
    </div>
  </article>

  <article class="card" style="left:613px">
    <div class="card-photo" role="img" aria-label="Meeting room with a long conference table, blue chairs and projector screen" style="background:linear-gradient(180deg,#d9dbe0 0%,#b5b8bf 45%,#3b4463 75%,#6e6a62 100%)"></div>
    <div class="card-body">
      <h3 class="card-name">Large Meeting Room</h3>
      <p class="card-desc">A delightful, spacious room with an outlook and access to the small walled garden. Ideal for meetings and small gatherings - it has its own access door and the use of a disabled W/C. We offer a reduced rate for this room when booked together with the main hall.</p>
      <p class="card-meta"><b>Capacity:</b> 20 People<br><b>Price:</b> £6-12 per hour</p>
      <div class="card-actions"><span class="link-more">More Info</span><span class="link-book">Book Now</span></div>
    </div>
  </article>
</section>

<footer class="site-footer">
  <div class="brand"><span class="brand-mark"></span>Marlowick Community Hall</div>
  <p class="abs footer-blurb">Lorem ipsum dolor sit amet, consectetur adipiscing elit, sed do eiusmod tempor incididunt ut labore et dolore magna aliqua.</p>
  <div class="footer-col" style="left:420px">
    <h4>SITE MAP</h4>
    <ul><li>Home</li><li>Calendar</li><li>Facilities</li><li>Prices</li><li>Photos</li><li>News</li><li>Contact</li></ul>
  </div>
  <div class="footer-col" style="left:586px">
    <h4>QUICK LINKS</h4>
    <ul><li>Login</li><li>Register</li><li>Privacy Policy</li><li>Terms &amp; Conditions</li></ul>
  </div>
  <div class="footer-col" style="left:780px">
    <h4>OUR CONTACTS</h4>
    <ul class="contact-list">
      <li><svg viewBox="0 0 16 16" fill="#fff"><path d="M3.5 1.5l2.5 0 1.2 3.2-1.6 1.2a8 8 0 0 0 4.5 4.5l1.2-1.6 3.2 1.2v2.5a1.5 1.5 0 0 1-1.6 1.5A12 12 0 0 1 2 3.1 1.5 1.5 0 0 1 3.5 1.5z"/></svg>(000) 555-0199</li>
      <li><svg viewBox="0 0 16 16" fill="#fff"><path d="M1 3h14v10H1z"/><path d="M1 3l7 6 7-6" fill="none" stroke="#0e2d66" stroke-width="1.4"/></svg>bookings@marlowickhall.org</li>
      <li><svg viewBox="0 0 16 16" fill="#fff"><path d="M8 1a5 5 0 0 1 5 5c0 4-5 9-5 9S3 10 3 6a5 5 0 0 1 5-5z"/><circle cx="8" cy="6" r="2" fill="#0e2d66"/></svg>48 Elmbrook Lane, Marlowick MW4 2QT</li>
    </ul>
    <div class="social"><span><i></i>Chatterleaf</span><span><i></i>Quillcast</span></div>
  </div>
</footer>
<div class="legal">© 2021 Marlowick Community Hall. All rights reserved.</div>

</body>
</html>
```